Varnath Consulting Business card design.

See our website www.varnathconsulting-example.com which will give you a good idea of what we are about. The font is called 'Play'.

I'd like a standout business card in keeping with the themes and branding on the website

Target Market(s)

professionals. HR directors

Industry/Entity Type

Business

Contact Information for Business Card

Varnath Consulting PO Box 3917 Tindale Creek NSW 2840 1300 457 318 Gerald Ashbury Principal email: jobs@varnathconsulting-example.com ABN: 31792048663

Font styles to use
Other font styles liked:
• Play

Requirements
Must have
• Must have same design colours and branding as website.
• On back I'd prefer a list of the things we do which appears below the name at the header on the website

```html
<!DOCTYPE html>
<html lang="en">
<head>
<meta charset="utf-8">
<title>Varnath Consulting – Business Card</title>
<link rel="stylesheet" href="https://fonts.googleapis.com/css2?family=Play:wght@400;700&family=Arimo:wght@400;700&display=swap">
<style>
  :root {
    --page: #e9e9e7;
    --navy-deep: #0b1a2a;
    --navy: #142a40;
    --navy-soft: #1d3650;
    --blue: #2e9ee0;
    --ink: #1a1f26;
    --grey: #4a4f55;
    --grey-light: #9aa6b2;
    --paper: #ffffff;
    --paper-shade: #ececec;
  }
  * { box-sizing: border-box; margin: 0; padding: 0; }
  html, body { width: 1200px; height: 950px; overflow: hidden; }
  body {
    background: var(--page);
    display: flex;
    flex-direction: column;
    align-items: center;
    justify-content: center;
    gap: 50px;
    font-family: "Arimo", Arial, sans-serif;
  }
  .card {
    width: 700px;
    height: 400px;
    position: relative;
    overflow: hidden;
    box-shadow: 0 6px 18px rgba(0,0,0,0.18);
  }

  /* Front */
  .card-front {
    background: linear-gradient(160deg, var(--paper) 40%, var(--paper-shade) 100%);
  }
  .front-content { position: absolute; left: 52px; top: 46px; }
  .brand-name {
    font-family: "Play", sans-serif;
    font-weight: 400;
    letter-spacing: 3px;
    text-transform: uppercase;
  }
  .card-front .brand-name { font-size: 38px; color: var(--navy); }
  .person-name { margin-top: 30px; font-size: 23px; font-weight: 700; color: var(--ink); }
  .person-role { font-size: 17px; color: var(--blue); margin-top: 2px; }
  .contact-list { list-style: none; margin-top: 22px; font-size: 16px; color: var(--grey); line-height: 1.4; }
  .contact-list li { display: flex; align-items: center; gap: 8px; }
  .contact-list .address { display: block; max-width: 230px; margin-bottom: 2px; }
  .contact-icon { width: 15px; height: 15px; fill: var(--navy); flex: none; }

  .side-band {
    position: absolute; top: 0; right: 0; width: 112px; height: 100%;
    background: linear-gradient(180deg, var(--navy-soft), var(--navy-deep));
  }
  .side-band::before {
    content: ""; position: absolute; left: 6px; top: 0; width: 3px; height: 100%;
    background: var(--blue);
  }
  .band-url {
    position: absolute; left: 62px; top: 50%;
    transform: translate(-50%, -50%) rotate(-90deg);
    white-space: nowrap; font-size: 16px; letter-spacing: 1.5px; color: var(--blue);
  }

  /* Back */
  .card-back {
    background: linear-gradient(115deg, var(--navy-deep) 0%, var(--navy) 55%, var(--navy-soft) 100%);
  }
  .card-back .brand-name {
    position: absolute; left: 110px; top: 148px; font-size: 40px; color: var(--blue);
  }
  .service-list {
    position: absolute; right: 44px; top: 232px;
    list-style: none; display: flex; font-size: 16px; color: var(--grey-light);
  }
  .service-list li + li::before { content: "|"; color: var(--blue); margin: 0 10px; }
</style>
</head>
<body>
  <section class="card card-front" aria-label="Business card front">
    <div class="front-content">
      <p class="brand-name">Varnath Consulting</p>
      <p class="person-name">Gerald Ashbury</p>
      <p class="person-role">Principal</p>
      <ul class="contact-list">
        <li class="address">PO Box 3917 Tindale Creek NSW 2840</li>
        <li>
          <svg class="contact-icon" viewBox="0 0 16 16" aria-hidden="true"><path d="M2 5c0-2 2-3 6-3s6 1 6 3v1h-3V5H5v1H2zM4 7h8l2 6H2zm4 1.5a2 2 0 1 0 0 4 2 2 0 0 0 0-4z"/></svg>
          1300 457 318
        </li>
        <li>
          <svg class="contact-icon" viewBox="0 0 16 16" aria-hidden="true"><path d="M1 3h14v1L8 9 1 4zm0 2.5 7 5 7-5V13H1z"/></svg>
          jobs@varnathconsulting-example.com
        </li>
      </ul>
    </div>
    <div class="side-band">
      <span class="band-url">www.varnathconsulting-example.com</span>
    </div>
  </section>

  <section class="card card-back" aria-label="Business card back">
    <p class="brand-name">Varnath Consulting</p>
    <ul class="service-list">
      <li>Career Coaching</li>
      <li>Leadership</li>
      <li>Outplacement</li>
    </ul>
  </section>
</body>
</html>
```